Valdmont Construction Services
Building Modern Luxury
Valdmont Construction Services - Construction
Creative Brief
Construction
www.valsorvo.com
We specialize in Custom homes Commercial, Renovations, and metal buildings
We do not want a cluttery website. We want VERY modern with minimal text and Photos. Clean lines and not curves
High Tech
Black background and Black box
Greys, some white
some green
top
http://www.pinelakeestates.com/#home/
http://www.tolmanstudio.com/
We want a black background with a black rectangular box for the template(similar to pinelakeestates.com) We also want a Enter site page that jsut has our logo in the middle with Building Modern Luxury in white font and a Enter Here sign(like on Tolmanstudio.com but without photos) Maybe a dark grey siloette or outline of a house or roofs in the background(barely noticeable) integrated in the site. We want the second page to be the template page..preferbly a rectangular box that has a place for text and a place for a photo. We want our logo on each page. We want a tab for Home, Custom homes, commercial , renovations, metal buildings, and contact. We want the phone # to be on the top right on EVERY page 555 214 0376. We want our template to hold a place for text and a place for ONE photo( this photo box will be a slideshow for more photos) We want copyright info under the bottom of the rectangular template. We have also attached .a url of our logo and business card

```html
<!DOCTYPE html>
<html lang="en">
<head>
<meta charset="utf-8">
<title>Valdmont Construction Services — Enter</title>
<link href="https://fonts.googleapis.com/css2?family=Arimo:wght@400;700&display=swap" rel="stylesheet">
<style>
  :root {
    --bg: #000000;
    --frame: #8a8a8a;
    --white: #ffffff;
    --grey-mark: #6e6e6e;
    --button-fill: #1c1c1c;
    --footer-text: #4a4a4a;
    --house-tone: #151515;
  }
  html, body {
    margin: 0;
    padding: 0;
    width: 1200px;
    height: 744px;
    overflow: hidden;
    background: var(--bg);
    font-family: "Arimo", Arial, sans-serif;
  }
  .canvas {
    position: relative;
    width: 1200px;
    height: 744px;
    background: var(--bg);
  }
  .site-frame {
    position: absolute;
    left: 151px;
    top: 24px;
    width: 896px;
    height: 670px;
    border: 2px solid var(--frame);
    box-sizing: border-box;
  }
  .brand-mark {
    position: absolute;
    left: 509px;
    top: 58px;
    width: 182px;
    height: 182px;
    border-radius: 50%;
    background: var(--grey-mark);
  }
  .brand-name {
    position: absolute;
    left: 0;
    width: 1200px;
    top: 258px;
    text-align: center;
    color: var(--white);
    font-weight: 400;
    margin: 0;
  }
  .brand-name .primary {
    display: block;
    font-size: 80px;
    line-height: 84px;
    letter-spacing: 1px;
  }
  .brand-name .secondary {
    display: block;
    font-size: 21px;
    line-height: 26px;
    letter-spacing: 6px;
    margin-top: 4px;
  }
  .tagline {
    position: absolute;
    left: 0;
    width: 1200px;
    top: 414px;
    text-align: center;
    color: var(--white);
    font-weight: 700;
    font-size: 31px;
    letter-spacing: 0.5px;
    margin: 0;
  }
  .rooflines {
    position: absolute;
    left: 216px;
    top: 468px;
    width: 780px;
    height: 192px;
    background: linear-gradient(to bottom, rgba(21,21,21,0) 0%, var(--house-tone) 55%, rgba(21,21,21,0.4) 100%);
  }
  .enter-button {
    position: absolute;
    left: 487px;
    top: 550px;
    width: 226px;
    height: 45px;
    box-sizing: border-box;
    border: 2px solid var(--white);
    background: var(--button-fill);
    color: var(--white);
    font-size: 20px;
    line-height: 41px;
    text-align: center;
    text-decoration: none;
    letter-spacing: 0.5px;
  }
  .copyright {
    position: absolute;
    left: 0;
    width: 1200px;
    top: 666px;
    text-align: center;
    color: var(--footer-text);
    font-size: 11px;
    margin: 0;
  }
</style>
</head>
<body>
<main class="canvas">
  <div class="site-frame"></div>
  <div class="rooflines" role="img" aria-label="Faint outline of house rooftops in the background"></div>
  <div class="brand-mark" aria-hidden="true"></div>
  <h1 class="brand-name">
    <span class="primary">VALDMONT</span>
    <span class="secondary">CONSTRUCTION SERVICES</span>
  </h1>
  <p class="tagline">BUILDING MODERN LUXURY</p>
  <a class="enter-button" href="#">ENTER HERE</a>
  <p class="copyright">Copyright © 2011 VALDMONT CONSTRUCTION SERVICES. All Rights Reserved.</p>
</main>
</body>
</html>
```